Velira....One Word, One Breath

I would like a hologram or golden seed of life as my logo or something along those lines with my business name Velira and then underneath....One Word, One Breath. Maybe black background....I’m not sure.
On the back, a list of my offerings,
*Lantern of Stillness /Learning to Breathe
*Connection to Source/Self
*Life Changing/Developing
*Plant Medicine consultation
*Conscious Awareness
Velira_lumo@morvexmail.com
Kelmar: 0437215096
I want my card to look inviting, caring and loving....but with a deep dive into human consciousness 👁💫.
Show me what you got🙏🏽

Designs look the same

```html
<!DOCTYPE html>
<html lang="en">
<head>
<meta charset="utf-8">
<title>Velira – One Word, One Breath</title>
<link rel="stylesheet" href="https://fonts.googleapis.com/css2?family=Oswald:wght@400;500;600&family=Questrial&display=swap">
<style>
  :root {
    --gold-deep: #e2b23c;
    --gold-mid: #f4dc6a;
    --gold-light: #fbf5c8;
    --bronze: #8a4f1c;
    --ink: #1c1a1a;
    --panel: #232122;
    --ring-gold: #e9c65a;
  }
  * { margin: 0; padding: 0; box-sizing: border-box; }
  html, body { width: 1200px; height: 720px; overflow: hidden; background: #ffffff; }
  .card {
    position: relative;
    width: 1200px;
    height: 720px;
    overflow: hidden;
    background: linear-gradient(90deg, var(--gold-deep) 0%, var(--gold-mid) 40%, var(--gold-light) 62%, var(--gold-mid) 82%, var(--gold-deep) 100%);
    color: var(--ink);
  }
  .card__shapes { position: absolute; inset: 0; }
  .brand-mark {
    position: absolute;
    left: 48px; top: 277px;
    width: 396px; height: 396px;
    border-radius: 50%;
    border: 5px solid var(--ring-gold);
    display: flex; align-items: center; justify-content: center;
    font-family: "Questrial", sans-serif;
    font-size: 54px;
    color: var(--ring-gold);
    letter-spacing: 0.06em;
  }
  .brand-name {
    position: absolute;
    left: 620px; width: 472px; top: 52px;
    text-align: center;
    font-family: "Oswald", sans-serif;
    font-weight: 600;
    font-size: 90px;
    line-height: 1;
    letter-spacing: 0.28em;
    text-indent: 0.28em;
  }
  .tagline {
    position: absolute;
    left: 620px; width: 472px; top: 146px;
    text-align: center;
    font-family: "Oswald", sans-serif;
    font-weight: 500;
    font-size: 40px;
    line-height: 1;
  }
  .offerings { list-style: none; font-family: "Questrial", sans-serif; font-size: 28px; }
  .offerings li {
    position: absolute;
    line-height: 1;
    white-space: nowrap;
    transform: translateY(-50%);
  }
  .offerings li::before {
    content: "";
    position: absolute;
    left: -32px; top: 50%;
    width: 13px; height: 13px;
    margin-top: -6px;
    border-radius: 50%;
    background: var(--ink);
  }
  .contact {
    position: absolute;
    right: 92px;
    font-family: "Questrial", sans-serif;
    font-size: 30px;
    line-height: 1;
    transform: translateY(-50%);
  }
  .contact-icon {
    position: absolute;
    width: 46px; height: 46px;
    right: 27px;
    transform: translateY(-50%);
  }
</style>
</head>
<body>
<main class="card">
  <svg class="card__shapes" width="1200" height="720" viewBox="0 0 1200 720" aria-hidden="true">
    <defs>
      <linearGradient id="bronze-band" x1="0" y1="0" x2="1" y2="0">
        <stop offset="0" stop-color="#6e3b14"/>
        <stop offset="0.55" stop-color="#a8682a"/>
        <stop offset="1" stop-color="#e2b23c" stop-opacity="0"/>
      </linearGradient>
    </defs>
    <path class="bronze-band" d="M0 0 H360 C470 80 520 130 560 200 L0 200 Z" fill="url(#bronze-band)"/>
    <path class="dark-panel-edge" d="M0 0 H222 C460 128 606 405 606 720 H0 Z" fill="#0f0e0e"/>
    <path class="dark-panel" d="M0 0 H205 C446 130 592 405 592 720 H0 Z" fill="var(--panel)"/>
  </svg>

  <div class="brand-mark">Velira</div>

  <h1 class="brand-name">VELIRA</h1>
  <p class="tagline">One Word, One Breath.</p>

  <ul class="offerings">
    <li style="left:595px; top:317px;">Lantern of Stillness /Learning to Breathe</li>
    <li style="left:613px; top:365px;">Connection to Source/Self</li>
    <li style="left:627px; top:415px;">Life Changing/Developing</li>
    <li style="left:635px; top:466px;">Plant Medicine consultation</li>
    <li style="left:653px; top:520px;">Conscious Awareness</li>
  </ul>

  <p class="contact" style="top:616px;">Velira_lumo@morvexmail.com</p>
  <svg class="contact-icon" style="top:616px;" viewBox="0 0 46 46" aria-hidden="true">
    <circle cx="23" cy="23" r="21" fill="none" stroke="var(--ink)" stroke-width="2.5"/>
    <rect x="12" y="16" width="22" height="15" rx="1.5" fill="var(--ink)"/>
    <path d="M12.5 17 L23 25 L33.5 17" fill="none" stroke="var(--gold-mid)" stroke-width="1.6"/>
  </svg>

  <p class="contact" style="top:679px;">043/721 50 96</p>
  <svg class="contact-icon" style="top:679px;" viewBox="0 0 46 46" aria-hidden="true">
    <circle cx="23" cy="23" r="21" fill="none" stroke="var(--ink)" stroke-width="2.5"/>
    <path d="M16 12 l4 0 2 6 -3 2 c1.5 3.5 3.5 5.5 7 7 l2 -3 6 2 0 4 c0 2 -1.5 3 -3 3 C21 33 13 25 13 15 c0 -1.5 1 -3 3 -3 Z" fill="var(--ink)"/>
    <path d="M26 13 a8 8 0 0 1 7 7 M26 17 a4 4 0 0 1 3 3" fill="none" stroke="var(--ink)" stroke-width="1.8" stroke-linecap="round"/>
  </svg>
</main>
</body>
</html>
```